Financial Coaching biz needs modern service presentation menu

We need a PowerPoint presentation document with a modern, easy-to-read layout to share with potential clients.

I have a website under development that can be used as a reference www.brightledgerhub.com.

We'd like the doc to be simple to edit because services and verbiage will likely be modified periodically.

Two logo variations have been included.

Target Market(s)

Gen X, Gen Y, and Millienials

Industry/Entity Type

Financial Planning

Colors
85cae6
cadf82
ffffff
dddddd
cfcfcf
cee9f5

```html
<!DOCTYPE html>
<html lang="en">
<head>
<meta charset="utf-8">
<title>BrightLedger Hub – Service Menu</title>
<link href="https://fonts.googleapis.com/css2?family=Lato:wght@400;700&family=Open+Sans:wght@400;700&display=swap" rel="stylesheet">
<style>
  :root {
    --backdrop: #c4c4c4;
    --paper: #ffffff;
    --rule: #e2e2e2;
    --ink-grey: #6b6b6b;
    --logo-green: #2bb673;
    --plan-blue: #5d93c9;
    --plan-ink: #1f3f7a;
    --budget-red: #d0635c;
    --budget-ink: #c83f38;
    --credit-green: #a5c46a;
    --credit-ink: #98bf52;
    --asset-purple: #8c78b3;
    --asset-ink: #7657a6;
    --tax-teal: #5bb9d4;
    --tax-ink: #3aa7c9;
  }
  * { margin: 0; padding: 0; box-sizing: border-box; }
  html, body { width: 1200px; height: 930px; overflow: hidden; }
  body { background: var(--backdrop); position: relative; font-family: 'Lato', sans-serif; }

  .slide { position: absolute; left: 97px; top: 88px; width: 1006px; height: 754px; background: var(--paper); }

  .brand { position: absolute; left: 76px; top: 60px; display: flex; align-items: center; gap: 14px; }
  .brand-mark { width: 60px; height: 60px; border-radius: 50%; background: var(--logo-green); }
  .brand-name { font-family: 'Lato', sans-serif; font-weight: 700; font-size: 36px; line-height: 40px; color: var(--logo-green); letter-spacing: 0.5px; }

  .service { position: absolute; top: 203px; width: 165px; }
  .service-banner { position: relative; width: 165px; height: 205px; }
  .service-banner svg { position: absolute; inset: 0; }
  .service-points { position: absolute; left: 7px; right: 7px; top: 6px; height: 172px; display: flex; flex-direction: column; justify-content: center; gap: 15px; text-align: center; color: #fff; font-size: 14px; line-height: 15px; }
  .plan .service-points { left: 11px; right: 11px; }
  .service-icon { position: absolute; top: 232px; left: 50%; transform: translateX(-50%); }
  .service-title { position: absolute; top: 305px; left: 0; right: 0; text-align: center; font-weight: 700; font-size: 20.5px; line-height: 25px; }

  .plan { left: 76px; }   .plan .service-title { color: var(--plan-ink); }
  .budget { left: 249px; } .budget .service-title { color: var(--budget-ink); }
  .credit { left: 419px; } .credit .service-title { color: var(--credit-ink); }
  .asset { left: 589px; }  .asset .service-title { color: var(--asset-ink); }
  .tax { left: 758px; }    .tax .service-title { color: var(--tax-ink); }

  .divider { position: absolute; top: 417px; width: 1px; height: 172px; background: var(--rule); }

  .extras { position: absolute; left: 88px; top: 624px; font-family: 'Open Sans', sans-serif; font-size: 16.5px; line-height: 23px; color: var(--ink-grey); }
  .extras strong { font-weight: 700; }
  .extras .red { color: var(--budget-ink); }
  .extras .green { color: var(--credit-green); }
  .extras .teal { color: var(--tax-ink); }
  .extras .purple { color: var(--asset-ink); }

  .site { position: absolute; right: 80px; top: 699px; font-family: 'Open Sans', sans-serif; font-size: 15px; letter-spacing: 0.4px; color: #8a8a8a; }
</style>
</head>
<body>
<main class="slide">
  <div class="brand">
    <span class="brand-mark"></span>
    <span class="brand-name">BRIGHTLEDGER<br>HUB</span>
  </div>

  <section class="service plan">
    <div class="service-banner">
      <svg width="165" height="205" viewBox="0 0 165 205"><polygon points="0,0 165,0 165,170 82.5,205 0,170" fill="var(--plan-blue)"/></svg>
      <div class="service-points"><p>Establish full-year plan for spending and saving, including major purchases or events</p></div>
    </div>
    <svg class="service-icon" width="60" height="50" viewBox="0 0 60 50">
      <rect x="8" y="30" width="7" height="16" fill="var(--plan-blue)"/><rect x="19" y="22" width="7" height="24" fill="var(--plan-blue)"/><rect x="30" y="26" width="7" height="20" fill="var(--plan-blue)"/><rect x="41" y="18" width="7" height="28" fill="var(--plan-blue)"/>
      <rect x="3" y="46" width="50" height="2.5" fill="var(--plan-blue)"/>
      <polyline points="4,24 18,12 30,18 50,4" fill="none" stroke="var(--plan-blue)" stroke-width="3"/><polygon points="44,2 56,0 53,11" fill="var(--plan-blue)"/>
    </svg>
    <h2 class="service-title">Monetary<br>Action Plan</h2>
  </section>

  <div class="divider" style="left:245px"></div>

  <section class="service budget">
    <div class="service-banner">
      <svg width="165" height="205" viewBox="0 0 165 205"><polygon points="0,0 165,0 165,170 82.5,205 0,170" fill="var(--budget-red)"/></svg>
      <div class="service-points"><p>Unlimited consultations to determine holes and waste in spending</p><p>Client choice from multiple budgeting strategies to determine best personal fit</p></div>
    </div>
    <svg class="service-icon" width="58" height="58" viewBox="0 0 58 58">
      <circle cx="29" cy="29" r="26" fill="#c94a44"/>
      <path d="M29 29 L29 3 M29 29 L52 18 M29 29 L38 54 M29 29 L6 40" stroke="#fff" stroke-width="2"/>
    </svg>
    <h2 class="service-title">Budgeting<br>Service</h2>
  </section>

  <div class="divider" style="left:416px"></div>

  <section class="service credit">
    <div class="service-banner">
      <svg width="165" height="205" viewBox="0 0 165 205"><polygon points="0,0 165,0 165,170 82.5,205 0,170" fill="var(--credit-green)"/></svg>
      <div class="service-points"><p>Personalized assessment with ALL 3 bureaus</p><p>All Documentation provided for future use and personal records</p><p>Provide tools, knowledge, and strategy to prevent future missteps</p></div>
    </div>
    <svg class="service-icon" width="40" height="58" viewBox="0 0 40 58">
      <rect x="2" y="2" width="34" height="52" rx="3" fill="none" stroke="var(--credit-green)" stroke-width="3"/>
      <rect x="7" y="9" width="24" height="34" fill="none" stroke="var(--credit-green)" stroke-width="1.5"/>
      <polyline points="10,36 16,28 21,31 28,18" fill="none" stroke="var(--credit-green)" stroke-width="2"/>
      <circle cx="19" cy="48" r="2" fill="var(--credit-green)"/>
    </svg>
    <h2 class="service-title">BrightLedger's<br>Credit-Ed<br>Service</h2>
  </section>

  <div class="divider" style="left:587px"></div>

  <section class="service asset">
    <div class="service-banner">
      <svg width="165" height="205" viewBox="0 0 165 205"><polygon points="0,0 165,0 165,170 82.5,205 0,170" fill="var(--asset-purple)"/></svg>
      <div class="service-points"><p>Complimentary Rental and Mortgage Assessment</p><p>Quarterly Insurance Assessment</p><p>Quarterly Utility Assessment</p></div>
    </div>
    <svg class="service-icon" width="58" height="58" viewBox="0 0 58 58">
      <polygon points="29,2 56,16 2,16" fill="var(--asset-purple)"/>
      <circle cx="29" cy="11" r="3" fill="#fff"/>
      <rect x="5" y="18" width="48" height="4" fill="var(--asset-purple)"/>
      <rect x="10" y="24" width="8" height="22" fill="var(--asset-purple)"/><rect x="25" y="24" width="8" height="22" fill="var(--asset-purple)"/><rect x="40" y="24" width="8" height="22" fill="var(--asset-purple)"/>
      <rect x="4" y="48" width="50" height="4" fill="var(--asset-purple)"/><rect x="1" y="53" width="56" height="4" fill="var(--asset-purple)"/>
    </svg>
    <h2 class="service-title">Asset<br>Advocate</h2>
  </section>

  <div class="divider" style="left:755px"></div>

  <section class="service tax">
    <div class="service-banner">
      <svg width="165" height="205" viewBox="0 0 165 205"><polygon points="0,0 165,0 165,170 82.5,205 0,170" fill="var(--tax-teal)"/></svg>
      <div class="service-points"><p>Free prior year return review and amendment filing</p><p>Guarantee best price</p><p>Partnership discount applied with all future filings</p></div>
    </div>
    <svg class="service-icon" width="44" height="56" viewBox="0 0 44 56">
      <rect x="1" y="1" width="42" height="54" rx="2" fill="var(--tax-teal)"/>
      <text x="22" y="18" text-anchor="middle" font-family="Lato, sans-serif" font-weight="700" font-size="15" fill="#fff">TAX</text>
      <g fill="#fff"><rect x="6" y="24" width="32" height="3"/><rect x="6" y="30" width="32" height="3"/><rect x="6" y="36" width="32" height="3"/><rect x="6" y="42" width="32" height="3"/><rect x="6" y="48" width="32" height="3"/></g>
    </svg>
    <h2 class="service-title">Tax<br>Preparation</h2>
  </section>

  <p class="extras">Starbursts: <strong class="red">IN-PERSON BUDGET BUDDY SERVICE</strong><br><strong class="green">SAVINGS BUILDER</strong>, &nbsp;<strong class="teal">COUPON COMPANION</strong><br><strong class="purple">FREE VIP SEMINAR ACCESS</strong> and more!!!</p>

  <p class="site">www.brightledgerhub.com</p>
</main>
</body>
</html>
```